Gaming packaging design for headphones

We need a striking gaming packaging.

Two versions of the logo are attached. Use the one that seems better to you for your proposal.

We like special effects on packaging, such as UV print or similar.

We don’t want packaging with openings.

Target Market(s)

Gamers

Requirements
Must have
• - Technical specifications on 6 languages, below English version:
Speaker: 50MM
Impedance: 32Ω±15%
Sensitivity: 116dB±3db
Frequency Response: 20Hz to 20KHZ
Microphone: Ф6.0*5.0MM
Cable Length: 2.0M
Plug: 3.5MM*2+USB
Size: 180*110*210mm
Weight: 356g
Backlight: RGB

- Barcode

- Certificates (CE, RoHS)

```html
<!DOCTYPE html>
<html lang="en">
<head>
<meta charset="utf-8">
<title>Prime Clash Gaming Headphone Set – Packaging</title>
<link href="https://fonts.googleapis.com/css2?family=Russo+One&family=Teko:wght@600&family=Rajdhani:wght@500;700&display=swap" rel="stylesheet">
<style>
  :root {
    --stage: #161616;
    --panel: #2a2a2a;
    --panel-dark: #222222;
    --panel-side: #1f1f1f;
    --green: #4fa52d;
    --white: #f2f2f2;
    --muted: #bdbdbd;
    --line: #d8d8d8;
  }
  * { margin: 0; padding: 0; box-sizing: border-box; }
  html, body { width: 1200px; height: 674px; overflow: hidden; background: var(--stage); }
  .canvas { position: relative; width: 1200px; height: 674px; overflow: hidden; background: radial-gradient(ellipse at 50% 40%, #2c2c2c 0%, var(--stage) 70%); font-family: "Rajdhani", sans-serif; color: var(--white); }

  .panel { position: absolute; top: 90px; height: 500px; background: var(--panel); overflow: hidden; }

  .brand { display: flex; align-items: center; gap: 8px; font-family: "Rajdhani", sans-serif; font-weight: 700; letter-spacing: 1px; color: var(--white); white-space: nowrap; }
  .brand-mark { width: 14px; height: 14px; background: var(--green); }

  /* left side panel */
  .spine-panel { left: 20px; width: 92px; background: var(--panel-side); }
  .spine-title { position: absolute; left: 0; top: 18px; width: 92px; text-align: center; }
  .spine-gaming { font-family: "Teko", sans-serif; font-weight: 600; font-size: 30px; line-height: 26px; color: var(--green); letter-spacing: 1px; }
  .spine-set { font-family: "Rajdhani", sans-serif; font-weight: 700; font-size: 9px; line-height: 11px; color: var(--white); letter-spacing: 0.5px; }
  .spine-panel .headset-art { position: absolute; left: 16px; top: 70px; width: 60px; height: 200px; border-radius: 45%; background: radial-gradient(ellipse at 50% 60%, #5fb33a 0%, #c0392b 40%, #1a1a1a 70%, #141414 100%); }
  .specs { position: absolute; left: 8px; top: 285px; width: 76px; }
  .specs-head { font-weight: 700; font-size: 8px; line-height: 10px; color: var(--green); margin-bottom: 2px; }
  .specs-langs { font-size: 6px; line-height: 8px; color: var(--muted); margin-bottom: 3px; }
  .specs dl { font-size: 6px; line-height: 8.5px; }
  .specs dt { float: left; clear: left; color: var(--muted); width: 36px; }
  .specs dd { color: var(--white); white-space: nowrap; }
  .certs { position: absolute; left: 8px; bottom: 16px; display: flex; gap: 6px; }
  .cert { width: 22px; height: 16px; border: 1px solid var(--white); border-radius: 2px; }

  /* back panel */
  .back-panel { left: 112px; width: 450px; }
  .back-panel .brand { position: absolute; left: 140px; top: 40px; font-size: 20px; }
  .features-title { position: absolute; left: 40px; top: 78px; font-family: "Russo One", sans-serif; font-size: 44px; letter-spacing: 3px; color: var(--white); white-space: nowrap; }
  .back-panel .headset-art { position: absolute; left: 160px; top: 150px; width: 230px; height: 230px; border-radius: 46% 40% 42% 48%; background: radial-gradient(circle at 55% 58%, #5fb33a 0%, #c0392b 28%, #1a1a1a 52%, #111 100%); }
  .callouts { position: absolute; left: 0; top: 0; width: 450px; height: 500px; }
  .feature { position: absolute; width: 110px; padding: 4px 8px; border-left: 1px solid var(--line); border-right: 1px solid var(--line); }
  .feature h3 { font-family: "Rajdhani", sans-serif; font-weight: 700; font-size: 11px; color: var(--white); margin-bottom: 3px; }
  .feature ul { list-style: none; }
  .feature li { font-size: 6px; line-height: 8px; color: var(--muted); white-space: nowrap; }
  .feature li::before { content: "• "; }
  .f1 { left: 20px; top: 205px; }
  .f2 { left: 40px; top: 350px; }
  .f3 { left: 235px; top: 420px; }
  .f4 { left: 335px; top: 360px; }
  .f5 { left: 300px; top: 80px; }

  /* front panel */
  .front-panel { left: 600px; width: 400px; background: var(--panel-dark); }
  .title-stack { position: absolute; left: 22px; top: 40px; width: 110px; height: 330px; }
  .title-gaming { position: absolute; left: 48px; top: 0; transform-origin: left top; transform: rotate(90deg) translateY(-60px); font-family: "Teko", sans-serif; font-weight: 600; font-size: 84px; line-height: 60px; color: var(--green); letter-spacing: 4px; white-space: nowrap; }
  .title-set { position: absolute; left: 0; top: 0; transform-origin: left top; transform: rotate(90deg) translateY(-26px); font-family: "Rajdhani", sans-serif; font-weight: 700; font-size: 25px; line-height: 26px; color: var(--white); letter-spacing: 3px; white-space: nowrap; }
  .front-panel .headset-art { position: absolute; left: 135px; top: 50px; width: 250px; height: 330px; border-radius: 50% 50% 40% 40%; background: radial-gradient(circle at 55% 65%, #5fb33a 0%, #d05a2a 25%, #1b1b1b 50%, #121212 100%); }
  .base-band { position: absolute; left: 0; bottom: 0; width: 400px; height: 100px; background: #1c1c1c; }
  .front-panel .brand { position: absolute; left: 28px; bottom: 30px; font-size: 18px; }
  .platforms { position: absolute; right: 36px; bottom: 28px; display: flex; gap: 10px; }
  .platform { width: 50px; height: 38px; border-radius: 6px; background: var(--green); display: flex; align-items: center; justify-content: center; font-family: "Russo One", sans-serif; font-size: 16px; color: var(--white); }

  /* right side panel */
  .side-panel { left: 1000px; width: 160px; background: var(--panel-dark); }
  .side-band { position: absolute; inset: 0; background: var(--green); clip-path: polygon(20% 0, 100% 0, 100% 100%, 0 100%); }
  .side-name { position: absolute; left: 40px; top: 60px; transform-origin: left top; transform: rotate(90deg) translateY(-70px); font-family: "Rajdhani", sans-serif; font-weight: 700; font-size: 58px; line-height: 70px; color: var(--panel-dark); white-space: nowrap; letter-spacing: 2px; }
</style>
</head>
<body>
<div class="canvas">

  <section class="panel spine-panel">
    <div class="spine-title">
      <div class="spine-gaming">GAMING</div>
      <div class="spine-set">HEADPHONE SET</div>
    </div>
    <div class="headset-art" role="img" aria-label="Side view of the headset earcup with RGB ring light"></div>
    <div class="specs">
      <div class="specs-head">SPECIFICATIONS</div>
      <div class="specs-langs">EN · DE · FR · ES · IT · PL</div>
      <dl>
        <dt>Speaker</dt><dd>50MM</dd>
        <dt>Impedance</dt><dd>32Ω±15%</dd>
        <dt>Sensitivity</dt><dd>116dB±3dB</dd>
        <dt>Frequency</dt><dd>20Hz–20KHz</dd>
        <dt>Microphone</dt><dd>Ф6.0*5.0MM</dd>
        <dt>Cable</dt><dd>2.0M</dd>
        <dt>Plug</dt><dd>3.5MM*2+USB</dd>
        <dt>Size</dt><dd>180*110*210mm</dd>
        <dt>Weight</dt><dd>356g</dd>
        <dt>Backlight</dt><dd>RGB</dd>
      </dl>
    </div>
    <div class="certs">
      <div class="cert" aria-label="Certification mark"></div>
      <div class="cert" aria-label="Certification mark"></div>
    </div>
  </section>

  <section class="panel back-panel">
    <div class="brand"><span class="brand-mark"></span>PRIME CLASH</div>
    <h1 class="features-title">FEATURES</h1>
    <div class="headset-art" role="img" aria-label="Product render of the black gaming headset with RGB-lit honeycomb earcup and boom microphone"></div>

    <svg class="callouts" viewBox="0 0 450 500" aria-hidden="true">
      <g stroke="var(--line)" stroke-width="1" fill="none">
        <polyline points="230,192 230,215 130,215"/>
        <polyline points="260,380 150,380"/>
        <polyline points="290,352 290,420"/>
        <polyline points="305,325 335,360"/>
        <polyline points="360,140 395,150 415,150 420,170"/>
      </g>
      <g fill="var(--white)">
        <circle cx="230" cy="192" r="2.5"/>
        <circle cx="260" cy="380" r="2.5"/>
        <circle cx="290" cy="352" r="2.5"/>
        <circle cx="305" cy="325" r="2.5"/>
        <circle cx="420" cy="170" r="2.5"/>
      </g>
    </svg>

    <div class="feature f1"><h3>FEATURE1</h3><ul><li>Speaker 50mm drivers</li><li>Deep immersive bass</li><li>Crisp clear highs</li><li>Low distortion output</li></ul></div>
    <div class="feature f2"><h3>FEATURE2</h3><ul><li>Flexible boom microphone</li><li>Noise reducing capsule</li><li>Clear team chat</li><li>Easy mute control</li></ul></div>
    <div class="feature f3"><h3>FEATURE3</h3><ul><li>Braided cable 2.0m</li><li>Dual 3.5mm plugs</li><li>USB light power</li><li>Tangle free design</li></ul></div>
    <div class="feature f4"><h3>FEATURE4</h3><ul><li>Soft memory foam</li><li>Breathable ear cushions</li><li>Long session comfort</li><li>Light 356g weight</li></ul></div>
    <div class="feature f5"><h3>FEATURE5</h3><ul><li>Adjustable steel headband</li><li>Padded top support</li><li>Secure snug fit</li><li>Durable frame build</li></ul></div>
  </section>

  <section class="panel front-panel">
    <div class="title-stack">
      <div class="title-gaming">GAMING</div>
      <div class="title-set">HEADPHONE SET</div>
    </div>
    <div class="headset-art" role="img" aria-label="Product render of the gaming headset in three-quarter view with RGB ring light and microphone"></div>
    <div class="base-band"></div>
    <div class="brand"><span class="brand-mark"></span>PRIME CLASH</div>
    <div class="platforms">
      <div class="platform">PC</div>
      <div class="platform" aria-label="Console compatible"></div>
      <div class="platform" aria-label="Headset with microphone">
        <svg width="28" height="26" viewBox="0 0 28 26" fill="none" stroke="var(--white)" stroke-width="2.2" stroke-linecap="round">
          <path d="M5 15 V12 a9 9 0 0 1 18 0 V15"/>
          <rect x="3" y="13" width="5" height="8" rx="2"/>
          <rect x="20" y="13" width="5" height="8" rx="2"/>
          <path d="M6 21 q2 4 8 3"/>
        </svg>
      </div>
    </div>
  </section>

  <section class="panel side-panel">
    <div class="side-band"></div>
    <div class="side-name">PRIME CLASH</div>
  </section>

</div>
</body>
</html>
```